creating a certificate for our flagship course

Hi,
We need a new certificate for our flagship course called Bright Harbour. We have been running this course for 25 years this year and want to get something special that represents that. We need our logos incorporated and we love to have a compass or Koru incorporated in the certificate. We like something different from your standard certificate, but not too crazy.

The text should say something along the lines of:
This certificate is awarded to ....
For successfully completing and contributing to the three day Bright Harbour programme.

signed:... date:...

to learn a bit more about this course and our company, please check our website. www.hollisvantreeve.co.nz

Thank you!

Target Market(s)

attendees who completed our 3 day programme.

Requirements
Must have
• Both our BH logo and our brand logo. a compass or a koru.
• a 25th year existence something on it.

```html
<!DOCTYPE html>
<html lang="en">
<head>
<meta charset="utf-8">
<title>Certificate of Completion – Bright Harbour</title>
<link rel="stylesheet" href="https://fonts.googleapis.com/css2?family=Open+Sans:ital,wght@0,400;0,700;1,400;1,600&family=Pinyon+Script&family=Roboto:wght@400&display=swap">
<style>
  :root {
    --stage: #222222;
    --paper: #ffffff;
    --green-dark: #6d9b2a;
    --green-light: #96c647;
    --green-line: #7fb63a;
    --green-script: #5e9a1e;
    --ink: #111111;
    --navy: #2b2d44;
    --grey-text: #4a4a4a;
  }
  * { box-sizing: border-box; margin: 0; padding: 0; }
  html, body {
    width: 1200px; height: 1000px; overflow: hidden;
    background: var(--stage);
  }
  .canvas { position: relative; width: 1200px; height: 1000px; }
  .certificate {
    position: absolute; left: 84px; top: 142px;
    width: 1031px; height: 796px;
    background: var(--paper); overflow: hidden;
  }
  .decor { position: absolute; left: -84px; top: -142px; }
  .content { position: absolute; inset: 0; text-align: center; }

  .company {
    position: absolute; left: 0; right: 0; top: 206px;
    display: flex; justify-content: center; align-items: center; gap: 12px;
  }
  .company-square { width: 56px; height: 56px; background: var(--navy); flex: none; }
  .company-name {
    font-family: "Open Sans", sans-serif; font-weight: 400;
    color: var(--navy); font-size: 18px; letter-spacing: 1.2px;
    line-height: 1.3; text-align: left;
  }

  .title {
    position: absolute; left: 0; right: 0; top: 292px;
    font-family: "Pinyon Script", cursive; font-weight: 400;
    font-size: 57px; color: var(--green-script); line-height: 1;
  }
  .awarded {
    position: absolute; left: 0; right: 0; top: 390px;
    font-family: "Open Sans", sans-serif; font-style: italic;
    font-size: 19px; color: var(--ink);
  }
  .recipient {
    position: absolute; left: 331px; width: 352px; top: 444px;
    font-family: "Open Sans", sans-serif; font-weight: 700;
    font-size: 32px; color: var(--ink); line-height: 1.2;
    padding-bottom: 7px; border-bottom: 3px solid var(--green-line);
  }
  .reason {
    position: absolute; left: 0; right: 0; top: 505px;
    font-family: "Open Sans", sans-serif; font-style: italic;
    font-size: 16px; line-height: 1.45; color: var(--ink);
  }
  .anniversary {
    position: absolute; left: 0; right: 0; top: 572px;
    display: flex; justify-content: center; align-items: center; gap: 8px;
    font-family: "Open Sans", sans-serif; font-style: italic; font-weight: 600;
    font-size: 13px; color: var(--green-script); letter-spacing: 0.5px;
  }

  .sign-field {
    position: absolute; top: 650px; width: 150px;
    border-top: 1.5px solid var(--green-line);
    font-family: "Open Sans", sans-serif; font-style: italic; font-weight: 600;
    font-size: 13px; color: var(--ink); padding-top: 5px;
  }
  .sign-field.date { left: 210px; }
  .sign-field.signature { left: 666px; }

  .programme {
    position: absolute; left: 417px; top: 623px;
    display: flex; align-items: center; gap: 10px;
  }
  .programme-square { width: 50px; height: 50px; background: var(--green-light); }
  .programme-name {
    font-family: "Roboto", sans-serif; font-weight: 400;
    font-size: 20px; color: var(--grey-text);
  }
</style>
</head>
<body>
<main class="canvas">
  <section class="certificate">
    <svg class="decor" width="1200" height="1000" viewBox="0 0 1200 1000">
      <defs>
        <linearGradient id="greenWash" x1="0" y1="0" x2="1" y2="1">
          <stop offset="0" stop-color="#6d9b2a"/>
          <stop offset="1" stop-color="#96c647"/>
        </linearGradient>
      </defs>
      <g class="frame" stroke="var(--green-line)" stroke-width="3" fill="none" aria-hidden="true">
        <polyline points="410,229 171,229 171,760"/>
        <polyline points="760,229 1025,229 1025,765"/>
        <line x1="258" y1="852" x2="940" y2="852"/>
      </g>
      <polygon class="decor-top" role="img" aria-label="Green geometric decoration along the top edge"
        points="323,142 845,142 760,228 673,312 586,228 498,312 410,228" fill="url(#greenWash)"/>
      <polygon class="decor-bottom-left" role="img" aria-label="Green geometric decoration in the lower left corner"
        points="84,678 258,850 344,938 84,938" fill="url(#greenWash)"/>
      <polygon class="decor-bottom-right" role="img" aria-label="Green geometric decoration in the lower right corner"
        points="1115,680 1115,938 856,938 940,852 1028,765" fill="url(#greenWash)"/>
    </svg>

    <div class="content">
      <div class="company">
        <span class="company-square"></span>
        <span class="company-name">HOLLIS<br>VANTREEVE &amp; Associates</span>
      </div>
      <h1 class="title">Certificate of Completion</h1>
      <p class="awarded">This certificate is awarded to</p>
      <p class="recipient">AMELIA THORNTON</p>
      <p class="reason">For successfully completing and contributing to the three day<br>Bright Harbour programme.</p>
      <p class="anniversary">
        <svg class="koru" width="20" height="20" viewBox="0 0 20 20" aria-hidden="true">
          <path d="M10 19 C10 12 3 12 3 7 C3 3 7 1 10 1 C14 1 17 4 17 8 C17 11 14 13 11.5 12 C9.5 11 9.5 8 11.5 7.5 C13 7.2 14 8.5 13 9.5"
            fill="none" stroke="var(--green-line)" stroke-width="1.8" stroke-linecap="round"/>
        </svg>
        Celebrating 25 years of Bright Harbour
      </p>
      <div class="sign-field date">Date</div>
      <div class="programme">
        <span class="programme-square"></span>
        <span class="programme-name">Bright Harbour</span>
      </div>
      <div class="sign-field signature">Signature</div>
    </div>
  </section>
</main>
</body>
</html>
```